Water Filter Company Needs an amazing brochure!!!

We made a logo on here, we are getting business cards on here, now its time for a brochure. We are a whole home water filter company, that is disrupting the industry by selling our units 1000's cheaper than the competition, all the while making a better unit. I need an informative brochure that highlights our company, and our two main products, and a few reasons to do business with us. I made a little pdf with some info on it, and am here if you have any questions! may the best designer win!
Updates

So a lot of people are confusing the two units, and it may be my fault, I need to revisit the PDF i uploaded on how the information is presented, but no worries, right now I am basing all of my ratings on the design, color scheme, and layout more than the content per se. ****** Also, the website is JUST Brevonix.com I know in the logo it says watersystems.. You everyone who submitted something with www.brevonixpurestream.com, could please edit that to just say www.brevonix.com I would greatly appreciate it. Me and my partner had a major argument over this logo in the past and I dont want to revisit that talk with him again lol. Thank you. Good work guys!!

Target Market(s)

Homeowners, people who are tired of buying bottled water, people who dont want to bathe and shower in chlorine. People who are just real health conscious. Stuff like that.

Industry/Entity Type

Water Purification

Font styles to use
Serif
Sans Serif

Requirements
Must have
• My logo. A showcase of my two products. Spot for QR code. Talk about having your water tested at the qrt.org/pipecheck

uses the color #192841 behind my logos or black.

Not a big fan of white spaces. Tri-Fold 8.5x11
Nice to have
• **Update, I just added several pictures of the business cards being designed right now, and the ones that have a shot at winning. For reference.

I laid out a bunch of stuff in the PDF. Ask questions if you have them.

It would be nice to have the best brochure in the world.

I do have an active project going on now, maybe you can check out the top ones to fit some kind of theme. Just an idea.

```html
<!DOCTYPE html>
<html lang="en">
<head>
<meta charset="utf-8">
<title>Brevonix Tri-Fold Brochure</title>
<link href="https://fonts.googleapis.com/css2?family=Montserrat:wght@500;700;800;900&family=Open+Sans:wght@400;600&display=swap" rel="stylesheet">
<style>
:root{
  --navy:#192841;
  --ink:#0e1a2e;
  --cyan:#2aa8e0;
  --text:#3a4656;
  --paper:#ffffff;
  --stage:#eef0f3;
  --rule:#e3e7ec;
}
*{box-sizing:border-box;margin:0;padding:0}
html,body{width:800px;height:1200px;overflow:hidden;background:var(--stage)}
body{position:relative;font-family:"Open Sans",Arial,sans-serif;color:var(--text)}
.spread{position:absolute;left:30px;width:740px;height:572px;background:var(--paper);display:flex;box-shadow:0 4px 18px rgba(0,0,0,.18);overflow:hidden}
.spread--outside{top:18px}
.spread--inside{top:610px}
.panel{position:relative;width:246.67px;height:100%;overflow:hidden}
.panel + .panel{border-left:1px solid var(--rule)}
.heading{font-family:"Montserrat",Arial,sans-serif;font-weight:800;font-size:12px;color:var(--navy);text-transform:uppercase;letter-spacing:.3px;margin-bottom:8px}
.heading em{font-style:normal;color:var(--cyan)}
.copy{font-size:7.6px;line-height:1.55;margin-bottom:9px}
.ticks{list-style:none}
.ticks li{position:relative;padding-left:13px;font-size:7.4px;line-height:1.45;margin-bottom:6px}
.ticks li::before{content:"";position:absolute;left:0;top:2px;width:8px;height:8px;border-radius:50%;background:var(--cyan)}
.ticks li::after{content:"";position:absolute;left:2.3px;top:3.6px;width:3px;height:2px;border-left:1.3px solid #fff;border-bottom:1.3px solid #fff;transform:rotate(-45deg)}
.pad{padding:22px 20px}
.brand{display:flex;align-items:center;gap:6px;font-family:"Montserrat",Arial,sans-serif;font-weight:800;font-size:17px;color:var(--cyan)}
.brand::before{content:"";width:12px;height:12px;border-radius:50%;background:var(--cyan)}
.photo{position:absolute;left:0;width:100%}
.wave{position:absolute;left:0;width:100%}

/* outside: left flap */
.flap .ticks li{margin-bottom:8px}
.test-box{position:absolute;left:18px;right:18px;bottom:20px;background:var(--navy);color:#fff;padding:14px;border-radius:4px;display:flex;gap:10px;align-items:center}
.test-box p{font-size:7.6px;line-height:1.5}
.test-box strong{display:block;font-family:"Montserrat",Arial,sans-serif;font-size:10px;color:var(--cyan);margin-bottom:3px}
.qr-spot{flex:0 0 48px;height:48px;background:#fff;border-radius:3px}

/* outside: back panel */
.back .header{position:absolute;top:0;left:0;width:100%;height:96px;background:var(--navy)}
.back .circle-photo{position:absolute;top:28px;left:50%;margin-left:-62px;width:124px;height:124px;border-radius:50%;border:5px solid var(--cyan);background:radial-gradient(circle,#f1f4f8,#9fb3c8)}
.back .brand{position:absolute;top:172px;left:0;right:0;justify-content:center;font-size:22px}
.contact{position:absolute;top:222px;left:24px;right:24px}
.contact .label{font-family:"Montserrat",Arial,sans-serif;font-weight:800;font-size:11px;color:var(--navy);letter-spacing:.5px}
.contact .phone{font-family:"Montserrat",Arial,sans-serif;font-weight:800;font-size:19px;color:var(--cyan);margin:2px 0 16px}
.contact-row{display:flex;align-items:center;gap:9px;font-size:8.2px;margin-bottom:12px;color:var(--navy)}
.contact-row .ic{flex:0 0 20px;height:20px;border-radius:50%;background:var(--navy);display:flex;align-items:center;justify-content:center}
.back .foot{position:absolute;bottom:0;left:0;width:100%;height:46px}

/* outside: cover */
.cover .photo{top:0;height:330px;background:radial-gradient(circle at 50% 55%,#3a7fb8 0%,#17304f 45%,#050a12 100%)}
.cover .brand{position:absolute;top:20px;left:0;right:0;justify-content:center;color:#fff}
.cover-title{position:absolute;left:22px;top:362px;font-family:"Montserrat",Arial,sans-serif;font-weight:900;line-height:1.05}
.cover-title .big{font-size:30px;color:var(--navy);display:block}
.cover-title .sub{font-size:15px;color:var(--cyan);display:block;margin-top:4px}
.cover-url{position:absolute;right:18px;bottom:16px;font-size:8.5px;font-weight:600;color:#fff;z-index:2}

/* inside: left */
.intro .lower-photo{top:330px;height:242px;background:linear-gradient(135deg,#c9ccd2,#8a7f78 55%,#5b6b80)}
/* inside: middle */
.products .top{position:absolute;top:0;left:0;width:100%;height:250px;background:var(--navy);padding:22px 18px}
.products .top .heading{color:#fff}
.product{display:flex;gap:10px;align-items:center;margin-bottom:14px}
.product .thumb{flex:0 0 62px;height:62px;border-radius:50%;border:3px solid var(--cyan);background:radial-gradient(circle,#f3f6f9,#b9c7d6)}
.product h4{font-family:"Montserrat",Arial,sans-serif;font-size:9px;font-weight:800;color:#fff;margin-bottom:3px;text-transform:uppercase}
.product p{font-size:7.2px;line-height:1.5;color:#d6e2ee}
.products .mid-photo{top:250px;height:170px;background:linear-gradient(135deg,#b7462f,#8f98a4 45%,#4c5d73)}
.products .below{top:440px}
/* inside: right */
.worker-photo{top:0;height:225px;background:linear-gradient(135deg,#e7e2d6,#c7b98f 45%,#6f7f92)}
.below{position:absolute;top:262px;left:20px;right:20px}
.intro .below{top:24px}
</style>
</head>
<body>

<section class="spread spread--outside">
  <article class="panel flap pad">
    <h2 class="heading">Why Filter <em>Your Water?</em></h2>
    <p class="copy">City water carries chlorine, sediment and traces you cannot see. One whole home unit cleans every tap, shower and appliance at once.</p>
    <ul class="ticks">
      <li>Removes chlorine for softer skin and hair in every shower.</li>
      <li>No more hauling cases of bottled water home.</li>
      <li>Protects pipes, heaters and appliances from buildup.</li>
      <li>Better tasting water for cooking and coffee.</li>
      <li>Low upkeep with simple yearly service.</li>
      <li>Built to last and priced far below big brands.</li>
      <li>Local install team and friendly support.</li>
      <li>Free in-home water test before you buy.</li>
      <li>Flexible payment plans for every budget.</li>
      <li>Trusted by hundreds of local families.</li>
    </ul>
    <div class="test-box">
      <div class="qr-spot" role="img" aria-label="QR code spot"></div>
      <p><strong>Test Your Water</strong>See what is in your tap water at qrt.org/pipecheck</p>
    </div>
  </article>

  <article class="panel back">
    <div class="header"></div>
    <div class="circle-photo" role="img" aria-label="Photo of a whole home filter tank"></div>
    <div class="brand">Brevonix</div>
    <div class="contact">
      <div class="label">CONTACT US</div>
      <div class="phone">(480) 555-0162</div>
      <div class="contact-row"><span class="ic"><svg width="10" height="10" viewBox="0 0 24 24"><path fill="#fff" d="M12 2a7 7 0 0 0-7 7c0 5 7 13 7 13s7-8 7-13a7 7 0 0 0-7-7zm0 9.5A2.5 2.5 0 1 1 12 6.5a2.5 2.5 0 0 1 0 5z"/></svg></span>1200 Meridian Ave, Mesa, AZ 85201</div>
      <div class="contact-row"><span class="ic"><svg width="10" height="10" viewBox="0 0 24 24"><path fill="#fff" d="M3 5h18v14H3z"/><path d="M3 5l9 7 9-7" stroke="#192841" stroke-width="2" fill="none"/></svg></span>hello@brevonix.com</div>
      <div class="contact-row"><span class="ic"><svg width="10" height="10" viewBox="0 0 24 24"><circle cx="12" cy="12" r="9" fill="none" stroke="#fff" stroke-width="2"/><path d="M3 12h18M12 3c3 3 3 15 0 18M12 3c-3 3-3 15 0 18" stroke="#fff" stroke-width="1.6" fill="none"/></svg></span>www.brevonix.com</div>
    </div>
    <svg class="foot" viewBox="0 0 247 46" preserveAspectRatio="none"><path d="M0 20 Q90 0 247 22 V46 H0z" fill="#2aa8e0"/><path d="M0 30 Q110 12 247 32 V46 H0z" fill="#192841"/></svg>
  </article>

  <article class="panel cover">
    <div class="photo" role="img" aria-label="Photo of a whole home filter tank in a splash of water"></div>
    <div class="brand">Brevonix</div>
    <svg class="wave" style="top:290px;height:70px" viewBox="0 0 247 70" preserveAspectRatio="none"><path d="M0 40 Q120 0 247 30 V70 H0z" fill="#2aa8e0"/><path d="M0 52 Q130 14 247 44 V70 H0z" fill="#fff"/></svg>
    <h1 class="cover-title"><span class="big">WE ARE</span><span class="sub">A WHOLE HOME<br>WATER FILTER<br>COMPANY</span></h1>
    <svg class="wave" style="bottom:0;height:90px" viewBox="0 0 247 90" preserveAspectRatio="none"><path d="M60 90 Q170 70 247 0 V90z" fill="#2aa8e0"/><path d="M120 90 Q200 70 247 30 V90z" fill="#192841"/></svg>
    <div class="cover-url">www.brevonix.com</div>
  </article>
</section>

<section class="spread spread--inside">
  <article class="panel intro">
    <div class="below">
      <h2 class="heading">Who <em>We Are</em></h2>
      <p class="copy">We build whole home filters that beat the big names on quality and cost thousands less. Clean water should be simple and fair.</p>
      <ul class="ticks">
        <li>Family run and local to your area.</li>
        <li>Honest pricing with no hidden fees.</li>
        <li>Fast install, most homes in one day.</li>
        <li>Lifetime help from a real person.</li>
        <li>Units built to outlast the big brands.</li>
        <li>Free yearly check on every system.</li>
      </ul>
    </div>
    <div class="photo lower-photo" role="img" aria-label="Photo of a technician fitting a filter to home plumbing"></div>
    <svg class="wave" style="top:312px;height:50px" viewBox="0 0 247 50" preserveAspectRatio="none"><path d="M0 0 H247 V20 Q120 44 0 14z" fill="#fff"/><path d="M0 14 Q120 44 247 20 V28 Q120 52 0 22z" fill="#2aa8e0"/></svg>
  </article>

  <article class="panel products">
    <div class="top">
      <h2 class="heading">Our <em>Two Systems</em></h2>
      <div class="product">
        <div class="thumb" role="img" aria-label="Photo of the carbon filter tank"></div>
        <div><h4>Quorvale Carbon</h4><p>Removes chlorine, taste and odor from every tap in the home for years.</p></div>
      </div>
      <div class="product">
        <div class="thumb" role="img" aria-label="Photo of the softener filter tank"></div>
        <div><h4>Quorvale Soft Plus</h4><p>Filters and conditions hard water to stop scale on fixtures and heaters.</p></div>
      </div>
    </div>
    <div class="photo mid-photo" role="img" aria-label="Photo of a plumber working on home water pipes"></div>
    <div class="below">
      <ul class="ticks">
        <li>Both units built with certified grade media.</li>
        <li>Ten year tank warranty included.</li>
        <li>Thousands less than leading brands.</li>
        <li>Call (480) 555-0162 for a free quote.</li>
      </ul>
    </div>
  </article>

  <article class="panel">
    <div class="photo worker-photo" role="img" aria-label="Photo of an installer in a hard hat checking a system"></div>
    <svg class="wave" style="top:195px;height:60px" viewBox="0 0 247 60" preserveAspectRatio="none"><path d="M0 24 Q120 0 247 30 V60 H0z" fill="#192841"/><path d="M0 36 Q130 12 247 42 V60 H0z" fill="#fff"/></svg>
    <div class="below">
      <h2 class="heading">Whole Home <em>Protection</em></h2>
      <p class="copy">Every drop in your home runs through one system, from the kitchen sink to the shower head.</p>
      <ul class="ticks">
        <li>Safer water for kids and pets.</li>
        <li>Cleaner laundry and spot free dishes.</li>
        <li>Less plastic waste from bottles.</li>
        <li>Free water test before every install.</li>
        <li>Check your local report at qrt.org/pipecheck.</li>
        <li>Softer skin and hair after every shower.</li>
        <li>Longer life for heaters and appliances.</li>
      </ul>
    </div>
  </article>
</section>

</body>
</html>
```